Letterhead Design Project

I will upload my logo for this business letterhead.
I would like the logo on the top left
Top right, I would like two short columns - first short column would have business address: (possibly use some logo colors in the address)
PO Box 4172
Maple Ridge, FL 32251
Second short column would have all other business contact info:
(This info would be in a column to the RIGHT of the mailing address given above) possibly use some colors from the logo here also
Telephone 800.613.2274
Fax 386.537.1068
harriet@pinegroveformation.com
pinegroveformation.com
maybe a colored line at the bottom if you think it would look good

```html
<!DOCTYPE html>
<html lang="en">
<head>
<meta charset="utf-8">
<title>Pine Grove Formation — Letterhead</title>
<link rel="stylesheet" href="https://fonts.googleapis.com/css2?family=Mulish:wght@400;700&display=swap">
<style>
  :root {
    --backdrop: #ececec;
    --paper: #f5f5f5;
    --brand-red: #c8102e;
    --brand-orange: #f39200;
    --ink: #222222;
    --muted: #666666;
    --divider: #e08a8a;
  }
  * { box-sizing: border-box; margin: 0; padding: 0; }
  html, body {
    width: 1200px;
    height: 900px;
    overflow: hidden;
    background: var(--backdrop);
    font-family: "Mulish", "Helvetica Neue", Arial, sans-serif;
  }
  .canvas {
    position: relative;
    width: 1200px;
    height: 900px;
  }
  .letterhead {
    position: absolute;
    left: 377px;
    top: 121px;
    width: 446px;
    height: 632px;
    background: var(--paper);
  }
  .brand {
    position: absolute;
    left: 36px;
    top: 24px;
  }
  .brand-name {
    display: flex;
    align-items: center;
    gap: 8px;
    font-size: 11px;
    font-weight: 700;
    color: var(--brand-red);
    line-height: 1;
    white-space: nowrap;
  }
  .brand-dot {
    width: 10px;
    height: 10px;
    border-radius: 50%;
    background: var(--brand-orange);
  }
  .brand-tagline {
    margin-top: 3px;
    margin-left: 18px;
    font-size: 6px;
    color: var(--muted);
    white-space: nowrap;
  }
  .header-divider {
    position: absolute;
    left: 181px;
    top: 19px;
    width: 1px;
    height: 50px;
    background: var(--divider);
  }
  .address {
    position: absolute;
    left: 195px;
    top: 27px;
    font-size: 8.5px;
    line-height: 11px;
    color: var(--ink);
    font-style: normal;
    white-space: nowrap;
  }
  .contact {
    position: absolute;
    left: 294px;
    top: 24px;
    list-style: none;
    font-size: 8.5px;
    line-height: 10.5px;
    color: var(--ink);
    white-space: nowrap;
  }
  .contact-label {
    font-size: 6.5px;
    font-weight: 700;
    color: var(--brand-red);
    margin-right: 2px;
  }
  .footer-band {
    position: absolute;
    left: 0;
    bottom: 0;
    width: 100%;
    height: 10px;
    background: var(--brand-orange);
  }
</style>
</head>
<body>
<div class="canvas">
  <section class="letterhead">
    <header>
      <div class="brand">
        <div class="brand-name"><span class="brand-dot"></span>Pine Grove Formation</div>
        <div class="brand-tagline">a fresh path to formation</div>
      </div>
      <div class="header-divider"></div>
      <address class="address">
        PO Box 4172<br>
        Maple Ridge, FL 32251
      </address>
      <ul class="contact">
        <li><span class="contact-label">[P]</span>800.613.2274</li>
        <li><span class="contact-label">[F]</span>386.537.1068</li>
        <li><span class="contact-label">[E]</span>harriet@pinegroveformation.com</li>
        <li><span class="contact-label">[W]</span>www.pinegroveformation.com</li>
      </ul>
    </header>
    <div class="footer-band"></div>
  </section>
</div>
</body>
</html>
```